New business card with our logo

we finalized our logo with the help of pixel harbor - now we need a business card using that logo. we are a metal service center providing raw steel and metal products for fabricating, contractors, artists, etc. we have the wording for the back of the card figured out (attached, no deviations from text please), just need help putting it all together.
would like the look of steel somehow incorporated in the design ... would like the black part of the logo to be steel or silver color (the S & BRANLEY)
Other font styles liked:
- calibri, arial, similar to those, modern looking
Colors
Designer to choose colors to be used in the design.
Requirements
Must have
- Back of card must haves are attached (no deviations from wording please).
- FRONT of card:
- logo
- address
- name
- office tel
- cell
- fax
- website
- address
Nice to have
- incorporate the look of steel or element of steel somehow
- names of the staff on front not in all caps, i.e. Rosvita not ROSVITA
- this industry is more industrial, not coffee or flower shop so design should be aligned with that
- design should be classic and tasteful

```html
<!DOCTYPE html>
<html lang="en">
<head>
<meta charset="utf-8">
<title>Branley Steel – Business Card</title>
<link href="https://fonts.googleapis.com/css2?family=Montserrat:wght@400;500;600;700&display=swap" rel="stylesheet">
<style>
  :root {
    --backdrop: #2b2b2d;
    --card-blue: #0871b9;
    --white: #ffffff;
    --rule: rgba(255,255,255,0.9);
  }
  * { box-sizing: border-box; margin: 0; padding: 0; }
  html, body { width: 1200px; height: 960px; overflow: hidden; }
  body {
    background: var(--backdrop);
    font-family: "Montserrat", Arial, sans-serif;
    color: var(--white);
    position: relative;
  }
  .card {
    position: absolute;
    left: 281px;
    width: 655px;
    height: 374px;
    background: var(--card-blue);
    border-radius: 20px;
  }
  .card--front { top: 81px; }
  .card--back { top: 506px; }

  /* Front */
  .front-mark {
    position: absolute;
    left: 72px; top: 47px;
    width: 278px; height: 278px;
    border-radius: 50%;
    background: var(--white);
    display: flex; align-items: center; justify-content: center;
    text-align: center;
    color: var(--card-blue);
    font-weight: 700;
    font-size: 34px;
    line-height: 1.15;
    letter-spacing: 1px;
  }
  .contact { position: absolute; left: 396px; top: 58px; }
  .contact__name { font-size: 22px; font-weight: 600; letter-spacing: 0.2px; }
  .contact__title { font-size: 17px; font-weight: 400; margin-top: 5px; }
  .contact__company { font-size: 14.5px; font-weight: 700; margin-top: 22px; }
  .contact__address { font-size: 14.5px; line-height: 23px; margin-top: 2px; }
  .contact__list { list-style: none; margin-top: 14px; font-size: 14.5px; }
  .contact__list li { display: flex; align-items: center; height: 22px; }
  .contact__list svg { width: 12px; height: 12px; margin-right: 7px; flex: none; }

  /* Back */
  .brand { position: absolute; left: 115px; top: 64px; display: flex; align-items: center; }
  .brand__circle {
    width: 92px; height: 92px; border-radius: 50%;
    border: 5px solid var(--white);
    margin-right: 24px;
  }
  .brand__name { font-size: 46px; font-weight: 700; letter-spacing: -0.5px; }
  .services { position: absolute; left: 229px; top: 175px; font-size: 14px; }
  .services__heading { font-weight: 700; }
  .services p { line-height: 22px; }
  .services__rule { width: 65px; height: 1px; background: var(--rule); margin: 10px 0 10px 28px; }
</style>
</head>
<body>

<section class="card card--front">
  <div class="front-mark">BRANLEY<br>STEEL</div>
  <div class="contact">
    <h1 class="contact__name">Owen Carlisle</h1>
    <p class="contact__title">President &amp; CEO</p>
    <p class="contact__company">BranleySteel</p>
    <p class="contact__address">4180 Ridgeline Pkwy, Suite 210<br>Cary, NC 27513</p>
    <ul class="contact__list">
      <li><svg viewBox="0 0 12 12"><path d="M2 1l2 0 1 3-1.5 1a6 6 0 0 0 3.5 3.5L8 7l3 1v2c0 .6-.4 1-1 1A9 9 0 0 1 1 2c0-.6.4-1 1-1z" fill="#fff"/></svg>123.123.1234</li>
      <li><svg viewBox="0 0 12 12"><rect x="3" y="0.8" width="6" height="10.4" rx="1" fill="none" stroke="#fff" stroke-width="1.3"/><circle cx="6" cy="9.3" r=".7" fill="#fff"/></svg>123.123.1234</li>
      <li><svg viewBox="0 0 12 12"><rect x="3" y="1" width="6" height="3" fill="#fff"/><rect x="1" y="4.5" width="10" height="4.5" rx="1" fill="#fff"/><rect x="3" y="8" width="6" height="3" fill="#fff"/></svg>123.123.1234</li>
      <li><svg viewBox="0 0 12 12"><rect x="1" y="2.5" width="10" height="7" fill="#fff"/><path d="M1 2.5l5 4 5-4" fill="none" stroke="#0871b9" stroke-width="1"/></svg>info@BranleySteel.com</li>
      <li><svg viewBox="0 0 12 12"><g fill="none" stroke="#fff" stroke-width="1"><circle cx="6" cy="6" r="5"/><ellipse cx="6" cy="6" rx="2.2" ry="5"/><path d="M1 6h10M2 3.3h8M2 8.7h8"/></g></svg>www.BranleySteel.com</li>
    </ul>
  </div>
</section>

<section class="card card--back">
  <div class="brand">
    <span class="brand__circle"></span>
    <h2 class="brand__name">BRANLEY STEEL</h2>
  </div>
  <div class="services">
    <p class="services__heading">Metal Service Center</p>
    <p>Cut &nbsp;-&nbsp; Shear &nbsp;-&nbsp; Punch &nbsp;-&nbsp; Light Fab</p>
    <div class="services__rule"></div>
    <p>Structural Steel &nbsp;-&nbsp; Stainless &amp; Aluminum</p>
    <p>Building Components &nbsp;-&nbsp; Rebar &nbsp;-&nbsp; Decking and More!</p>
    <div class="services__rule"></div>
    <p>Cut to size, Pick-up or Delivered</p>
  </div>
</section>

</body>
</html>
```